Business Card Design

Hoping for a black background business card, minimalistic design.
With the Marble Crest logo you created in white.

I would like to include:
My Name and title
Address (street address)
Reception: (phone number)
Fax: (fax number)
Reception: (email address)
Direct email: (email address)
Instagram: (ig handle)

```html
<!DOCTYPE html>
<html lang="en">
<head>
<meta charset="utf-8">
<title>Marble Crest — Business Card</title>
<link rel="stylesheet" href="https://fonts.googleapis.com/css2?family=Montserrat:wght@700&family=Questrial&display=swap">
<style>
  :root {
    --stage: #8a8a8a;
    --card-front: #161616;
    --card-back: #050505;
    --ink-white: #f4f4f4;
    --ink-soft: #d8d8d8;
    --ink-emboss: #0a0a0a;
    --decor: #242424;
    --rule: #6a6a6a;
  }
  * { box-sizing: border-box; margin: 0; padding: 0; }
  html, body { width: 1200px; height: 900px; overflow: hidden; }
  body {
    background: var(--stage);
    font-family: "Questrial", sans-serif;
    position: relative;
  }
  .card {
    position: absolute;
    width: 700px;
    height: 400px;
    overflow: hidden;
  }
  .card--front {
    left: 250px; top: 30px;
    background: var(--card-front);
    border-radius: 36px 0 0 36px;
  }
  .card--back {
    left: 250px; top: 470px;
    background: var(--card-back);
    border-radius: 0 36px 0 36px;
  }
  .decor-circle {
    position: absolute;
    left: 330px; top: -190px;
    width: 360px; height: 360px;
  }
  .lockup {
    position: absolute;
    left: 40px; bottom: 40px;
    display: flex;
    align-items: center;
    gap: 18px;
  }
  .lockup__circle {
    width: 64px; height: 64px;
    border-radius: 50%;
    border: 4px solid currentColor;
  }
  .lockup__divider {
    width: 1px; height: 86px;
    background: currentColor;
    opacity: .7;
  }
  .lockup__name {
    font-size: 34px;
    letter-spacing: 4px;
    text-transform: uppercase;
  }
  .card--front .lockup { color: var(--ink-emboss); }
  .card--back .lockup { color: var(--ink-white); }

  .person {
    position: absolute;
    left: 42px; top: 40px;
    color: var(--ink-soft);
  }
  .person__name {
    font-family: "Montserrat", sans-serif;
    font-weight: 700;
    font-size: 17px;
    letter-spacing: .5px;
    text-transform: uppercase;
  }
  .person__title { font-size: 15px; margin-top: 3px; padding-left: 12px; }

  .contacts {
    position: absolute;
    left: 56px; top: 104px;
    list-style: none;
    color: var(--ink-white);
    font-size: 19px;
  }
  .contacts li {
    display: flex; align-items: center; gap: 10px;
    height: 27px;
  }
  .contacts svg { width: 16px; height: 16px; fill: var(--ink-soft); flex: none; }

  .rule {
    position: absolute;
    left: 250px; top: 262px;
    width: 390px; height: 1px;
    background: var(--rule);
  }
  .social {
    position: absolute;
    right: 40px; top: 176px;
    display: flex; align-items: center; gap: 8px;
    color: var(--ink-white);
    font-size: 17px;
  }
  .social__mark {
    width: 16px; height: 16px;
    border-radius: 4px;
    background: var(--ink-soft);
  }
</style>
</head>
<body>

  <section class="card card--front" aria-label="Card front">
    <svg class="decor-circle" viewBox="0 0 360 360" aria-hidden="true">
      <circle cx="180" cy="180" r="170" fill="none" stroke="var(--decor)" stroke-width="14"/>
    </svg>
    <div class="lockup">
      <div class="lockup__circle"></div>
      <div class="lockup__divider"></div>
      <div class="lockup__name">Marble Crest</div>
    </div>
  </section>

  <section class="card card--back" aria-label="Card back">
    <svg class="decor-circle" viewBox="0 0 360 360" aria-hidden="true">
      <circle cx="180" cy="180" r="170" fill="none" stroke="var(--decor)" stroke-width="14"/>
    </svg>

    <div class="person">
      <div class="person__name">Owen Hale</div>
      <div class="person__title">Director</div>
    </div>

    <ul class="contacts">
      <li>
        <svg viewBox="0 0 16 16" aria-label="Reception phone"><path d="M3 1h3l1.5 4-2 1.2a9 9 0 0 0 4.3 4.3L11 8.5l4 1.5v3a2 2 0 0 1-2 2A13 13 0 0 1 1 3a2 2 0 0 1 2-2z"/></svg>
        555-210-4800
      </li>
      <li>
        <svg viewBox="0 0 16 16" aria-label="Fax"><path d="M4 1h8v4H4zM1 6h14v7h-3v2H4v-2H1zM5 11v3h6v-3z"/></svg>
        555-310-4900
      </li>
      <li>
        <svg viewBox="0 0 16 16" aria-label="Reception email"><path d="M1 3h14v10H1zM2.5 4.5 8 9l5.5-4.5z"/></svg>
        info@marblecrest.com
      </li>
      <li>
        <svg viewBox="0 0 16 16" aria-label="Direct email"><path d="M1 3h14v10H1zM2.5 4.5 8 9l5.5-4.5z"/></svg>
        owen@marblecrest.com
      </li>
      <li>
        <svg viewBox="0 0 16 16" aria-label="Address"><path d="M8 0a5.5 5.5 0 0 1 5.5 5.5C13.5 10 8 16 8 16S2.5 10 2.5 5.5A5.5 5.5 0 0 1 8 0zm0 3.5a2 2 0 1 0 0 4 2 2 0 0 0 0-4z"/></svg>
        12 Harbor Lane, Easton 0400
      </li>
    </ul>

    <div class="social">
      <span>/marblecrest</span>
      <span class="social__mark" aria-hidden="true"></span>
    </div>

    <div class="rule"></div>

    <div class="lockup">
      <div class="lockup__circle"></div>
      <div class="lockup__divider"></div>
      <div class="lockup__name">Marble Crest</div>
    </div>
  </section>

</body>
</html>
```